Tidewell Gin - Label for new Gin bottle

I am looking for a bottle label for our small batch, handcrafted Gin. We are located in the bay-side city of Frankston (Victoria, Australia). I know I want more of a serious label but am torn between traditional or modern styling.

Label to include;
• Tidewell GIN (name)
• Hand Crafted
• Small Batch
• 40% Vol

Using 700ml MERIDA Spirit Bottle - Cork

Requirements
Must have
• Name; Tidewell Gin
Method: Hand Crafted
Batch Size; Small Batch
Alc; 40% Vol
Nice to have
• Maybe a coastal/seaside reference or reference to distilling.

```html
<!DOCTYPE html>
<html lang="en">
<head>
<meta charset="utf-8">
<title>Tidewell Gin — Bottle Label</title>
<link rel="stylesheet" href="https://fonts.googleapis.com/css2?family=Cinzel:wght@400;500&family=Playfair+Display:wght@700;800&display=swap">
<style>
  :root {
    --page: #ffffff;
    --label-navy: #0e4776;
    --botanical-blue: #2380c2;
    --ink-white: #ffffff;
    --batch-teal: #25b3c9;
    --shadow-navy: #072c4d;
  }
  html, body {
    margin: 0;
    padding: 0;
    width: 1200px;
    height: 1200px;
    overflow: hidden;
    background: var(--page);
  }
  .canvas {
    position: relative;
    width: 1200px;
    height: 1200px;
  }
  .label {
    position: absolute;
    left: 227px;
    top: 134px;
    width: 776px;
    height: 943px;
    background: var(--label-navy);
    overflow: hidden;
    color: var(--ink-white);
  }
  .botanical {
    position: absolute;
    pointer-events: none;
  }
  .botanical--top-left {
    left: 0; top: 0; width: 300px; height: 270px;
    background: radial-gradient(ellipse at 35% 30%, rgba(35,128,194,0.55), rgba(35,128,194,0) 70%);
  }
  .botanical--top-right {
    right: 0; top: 0; width: 290px; height: 270px;
    background: radial-gradient(ellipse at 65% 35%, rgba(35,128,194,0.55), rgba(35,128,194,0) 70%);
  }
  .botanical--bottom-left {
    left: 0; bottom: 0; width: 150px; height: 330px;
    background: radial-gradient(ellipse at 30% 60%, rgba(35,128,194,0.5), rgba(35,128,194,0) 70%);
  }
  .botanical--bottom-right {
    right: 0; bottom: 0; width: 250px; height: 330px;
    background: radial-gradient(ellipse at 60% 70%, rgba(35,128,194,0.5), rgba(35,128,194,0) 70%);
  }
  .frame {
    position: absolute;
    left: 23px; top: 23px; right: 23px; bottom: 23px;
    border: 1px solid var(--ink-white);
  }
  .tagline {
    position: absolute;
    left: 0; width: 100%;
    text-align: center;
    font-family: "Cinzel", serif;
    font-weight: 400;
    margin: 0;
  }
  .tagline--premium {
    top: 180px;
    font-size: 32px;
    letter-spacing: 0.5px;
  }
  .brand-name {
    position: absolute;
    left: 0; width: 100%;
    text-align: center;
    font-family: "Playfair Display", serif;
    font-weight: 700;
    margin: 0;
    line-height: 1;
    text-shadow: 3px 3px 0 var(--shadow-navy);
  }
  .brand-name--word {
    top: 250px;
    font-size: 100px;
    letter-spacing: -1px;
  }
  .brand-name--spirit {
    top: 370px;
    font-size: 178px;
    letter-spacing: -4px;
  }
  .batch-badge {
    position: absolute;
    left: 227px;
    top: 617px;
    width: 323px;
    height: 60px;
    background: var(--batch-teal);
    font-family: "Cinzel", serif;
    font-size: 33px;
    line-height: 60px;
    text-align: center;
    color: #eef9fb;
  }
  .tagline--method {
    top: 740px;
    font-size: 29px;
  }
  .details-rule {
    position: absolute;
    left: 79px;
    width: 619px;
    top: 795px;
    height: 1px;
    background: rgba(255,255,255,0.7);
  }
  .details-divider {
    position: absolute;
    top: 798px;
    width: 1px;
    height: 59px;
    background: rgba(255,255,255,0.7);
  }
  .details-divider--one { left: 284px; }
  .details-divider--two { left: 491px; }
  .strength {
    position: absolute;
    left: 94px;
    top: 806px;
    display: flex;
    align-items: center;
    font-family: "Playfair Display", serif;
  }
  .strength__value {
    font-family: "Cinzel", serif;
    font-size: 52px;
    line-height: 1;
  }
  .strength__unit {
    font-family: "Cinzel", serif;
    font-size: 19px;
    line-height: 1.15;
    margin-left: 8px;
  }
  .origin {
    position: absolute;
    left: 301px;
    top: 816px;
    display: flex;
    align-items: center;
  }
  .origin__map {
    width: 66px;
    height: 50px;
    background: rgba(255,255,255,0.85);
    border-radius: 10px;
  }
  .origin__text {
    font-family: "Cinzel", serif;
    font-size: 17px;
    line-height: 1.3;
    margin-left: 13px;
    letter-spacing: 0.5px;
  }
  .volume {
    position: absolute;
    left: 558px;
    top: 806px;
    font-family: "Cinzel", serif;
    display: flex;
    align-items: baseline;
  }
  .volume__value { font-size: 52px; line-height: 1; }
  .volume__unit { font-size: 18px; margin-left: 2px; }
</style>
</head>
<body>
<div class="canvas">
  <section class="label">
    <div class="botanical botanical--top-left" role="img" aria-label="Engraved botanical sprigs of juniper berries and lemon"></div>
    <div class="botanical botanical--top-right" role="img" aria-label="Engraved botanical sprigs of orange and star anise"></div>
    <div class="botanical botanical--bottom-left" role="img" aria-label="Engraved rosemary and juniper sprigs"></div>
    <div class="botanical botanical--bottom-right" role="img" aria-label="Engraved citrus slice, rosemary and spices"></div>

    <div class="frame"></div>

    <p class="tagline tagline--premium">PREMIUM QUALITY</p>
    <h1 class="brand-name brand-name--word">TIDEWELL</h1>
    <p class="brand-name brand-name--spirit">GIN</p>

    <div class="batch-badge">SMALL BATCH</div>

    <p class="tagline tagline--method">HAND CRAFTED &amp; COPPER DISTILLED</p>

    <div class="details-rule"></div>
    <div class="details-divider details-divider--one"></div>
    <div class="details-divider details-divider--two"></div>

    <div class="strength">
      <span class="strength__value">40%</span>
      <span class="strength__unit">ALC.<br>VOL.</span>
    </div>

    <div class="origin">
      <div class="origin__map" role="img" aria-label="Map outline of Australia"></div>
      <span class="origin__text">MADE IN<br>AUSTRALIA</span>
    </div>

    <div class="volume">
      <span class="volume__value">70</span>
      <span class="volume__unit">CL</span>
    </div>
  </section>
</div>
</body>
</html>
```